KPW Authorised Dealer needs Business Cards

We need a business card designed for our branch owners. Solvane Alarms is an Authorised KPW Dealer and does its own independent installations outside of the KPW work we perform so whilst the KPW Authorised Dealer Logo needs to be included, it should not be overwhelming in respect of the overall look of the card. I would like a rounded edge to the cards corners rather than a 90 degree hard edge. We also need to promote the fact that we do First Class Alarm & CCTV Solutions. (Details of card holder to follow)

```html
<!DOCTYPE html>
<html lang="en">
<head>
<meta charset="utf-8">
<title>Solvane Alarms – Business Cards</title>
<link rel="stylesheet" href="https://fonts.googleapis.com/css2?family=Open+Sans:wght@400;600;700&family=Oswald:wght@600&display=swap">
<style>
  :root {
    --bg: #e6e4e1;
    --card: #ffffff;
    --blue: #1b75bc;
    --blue-dark: #1a5f9e;
    --charcoal: #3a3b3d;
    --grey: #58595b;
    --text: #333333;
  }
  html, body {
    margin: 0;
    width: 1200px;
    height: 900px;
    overflow: hidden;
    background: var(--bg);
    font-family: "Open Sans", Arial, sans-serif;
  }
  .canvas { position: relative; width: 1200px; height: 900px; }

  .card {
    position: absolute;
    width: 620px;
    height: 354px;
    background: var(--card);
    border-radius: 16px;
    overflow: hidden;
    box-shadow: 0 6px 18px rgba(0,0,0,.18);
  }
  .card-bands { position: absolute; inset: 0; width: 100%; height: 100%; }

  .card--brand { left: 90px; top: 80px; }
  .card--contact { left: 490px; top: 466px; }

  .brand-mark {
    position: absolute;
    display: flex;
    flex-direction: column;
    align-items: center;
    gap: 14px;
  }
  .brand-mark__square {
    width: 44px; height: 44px;
    background: var(--blue);
  }
  .brand-mark__name {
    font-family: "Oswald", "Arial Narrow", sans-serif;
    font-weight: 600;
    font-size: 34px;
    letter-spacing: .5px;
    text-transform: uppercase;
    color: var(--blue);
    line-height: 1;
    white-space: nowrap;
  }
  .card--brand .brand-mark { left: 60px; top: 70px; }
  .card--contact .brand-mark { left: 44px; top: 110px; }

  .tagline {
    position: absolute;
    left: 60px; top: 196px;
    width: 250px;
    text-align: center;
    font-size: 13px;
    font-weight: 600;
    color: var(--grey);
  }

  .dealer-mark {
    position: absolute;
    right: 60px; top: 56px;
    display: flex; align-items: center; gap: 12px;
  }
  .dealer-mark__circle {
    width: 40px; height: 40px; border-radius: 50%;
    background: var(--blue-dark);
  }
  .dealer-mark__name {
    font-weight: 700; font-size: 34px; color: var(--blue-dark); line-height: 1;
  }

  .holder { position: absolute; left: 350px; top: 52px; }
  .holder__name { font-size: 20px; color: var(--blue); font-weight: 400; letter-spacing: .5px; }
  .holder__role { font-size: 13px; color: var(--text); margin-top: 2px; }

  .contact-list {
    position: absolute; left: 350px; top: 120px;
    margin: 0; padding: 0; list-style: none;
    font-size: 14px; color: var(--text); line-height: 1.35;
  }
  .contact-list li { display: flex; align-items: center; gap: 10px; }
  .contact-list .address { margin-bottom: 4px; letter-spacing: .5px; }
  .contact-list svg { width: 14px; height: 14px; fill: var(--blue); flex: none; }
</style>
</head>
<body>
<main class="canvas">

  <section class="card card--brand" aria-label="Card front">
    <svg class="card-bands" viewBox="0 0 620 354" preserveAspectRatio="none" aria-hidden="true">
      <rect x="0" y="0" width="620" height="22" fill="var(--charcoal)"/>
      <polygon points="150,354 620,190 620,354" fill="var(--blue)"/>
      <polygon points="120,354 620,176 620,186 150,354" fill="var(--blue-dark)"/>
    </svg>
    <div class="brand-mark">
      <span class="brand-mark__square"></span>
      <span class="brand-mark__name">Solvane Alarms</span>
    </div>
    <p class="tagline">First Class Alarm &amp; CCTV Solutions</p>
    <div class="dealer-mark">
      <span class="dealer-mark__circle"></span>
      <span class="dealer-mark__name">KPW</span>
    </div>
  </section>

  <section class="card card--contact" aria-label="Card back">
    <svg class="card-bands" viewBox="0 0 620 354" preserveAspectRatio="none" aria-hidden="true">
      <rect x="0" y="330" width="620" height="24" fill="var(--charcoal)"/>
      <polygon points="400,330 620,250 620,262 430,330" fill="var(--blue)"/>
    </svg>
    <div class="brand-mark">
      <span class="brand-mark__square"></span>
      <span class="brand-mark__name">Solvane Alarms</span>
    </div>

    <div class="holder">
      <div class="holder__name">Daniel Marsh</div>
      <div class="holder__role">Manager</div>
    </div>

    <ul class="contact-list">
      <li class="address">POX BOX 123 city,<br>123 country</li>
      <li>
        <svg viewBox="0 0 24 24"><path d="M6.6 10.8a15.1 15.1 0 0 0 6.6 6.6l2.2-2.2a1 1 0 0 1 1-.25 11.4 11.4 0 0 0 3.6.57 1 1 0 0 1 1 1V20a1 1 0 0 1-1 1A17 17 0 0 1 3 4a1 1 0 0 1 1-1h3.5a1 1 0 0 1 1 1c0 1.25.2 2.45.57 3.570a1 1 0 0 1-.25 1z"/></svg>
        111 222 333
      </li>
      <li>
        <svg viewBox="0 0 24 24"><path d="M7 1h10a2 2 0 0 1 2 2v18a2 2 0 0 1-2 2H7a2 2 0 0 1-2-2V3a2 2 0 0 1 2-2zm0 4v12h10V5zm5 14a1 1 0 1 0 0 2 1 1 0 0 0 0-2z"/></svg>
        111 222 333
      </li>
      <li>
        <svg viewBox="0 0 24 24"><path d="M2 5h20v14H2zm2 2v.5l8 5 8-5V7zm0 2.8V17h16V9.8l-8 5z"/></svg>
        info@solvanealarms.com
      </li>
      <li>
        <svg viewBox="0 0 24 24"><path d="M12 2a10 10 0 1 0 0 20 10 10 0 0 0 0-20zm6.9 9h-3a15 15 0 0 0-1.3-5.6A8 8 0 0 1 18.9 11zM12 4c.9 1.2 1.8 3.6 1.9 7h-3.8c.1-3.4 1-5.8 1.9-7zM9.4 5.4A15 15 0 0 0 8.1 11h-3a8 8 0 0 1 4.3-5.6zM5.1 13h3a15 15 0 0 0 1.3 5.6A8 8 0 0 1 5.1 13zM12 20c-.9-1.2-1.8-3.6-1.9-7h3.8c-.1 3.4-1 5.8-1.9 7zm2.6-1.4a15 15 0 0 0 1.3-5.6h3a8 8 0 0 1-4.3 5.6z"/></svg>
        www.solvanealarms.com
      </li>
    </ul>
  </section>

</main>
</body>
</html>
```